Travel Consultant Business Card

Hello.. New travel consultant looking seeking a business card that incorporates my new logo. I specialize in cruises but also want to imply land vacation. I am very open to any design and font concepts. I'm looking for a very upbeat modern design that reflects cruise and land vacations. Bright vibrant colors

Target Market(s)

Cruise and Land Vacationers

Industry/Entity Type

Travel Agent

Contact Information for Business Card

I am very open to any design and font concepts. I'm looking for a very upbeat modern design that reflects cruise and land vacations. Bright vibrant colors

Colors

Designer to choose colors to be used in the design.

Requirements
Must have
• Company Name: MapleRidge Journeys---New logo uploaded to be included in design
• My Name: Dolores Kwiatek-Travel Consultant
• Phone Number: (555) 418-7093
• E-Mail Address: mapleridgejourneys@examplemail.net
• Website: www.mapleridgejourneys.example
Nice to have
• My tag line is …..Here to Get You There

```html
<!DOCTYPE html>
<html lang="en">
<head>
<meta charset="utf-8">
<title>MapleRidge Journeys – Business Card</title>
<link rel="stylesheet" href="https://fonts.googleapis.com/css2?family=Roboto:wght@400;700&family=Roboto+Condensed:wght@700&display=swap">
<style>
  :root {
    --backdrop: #e4e4e4;
    --paper: #ffffff;
    --brand-blue: #0a5cb2;
    --sky-blue: #1aa8ea;
    --ink-grey: #555555;
    --rule-grey: #555555;
    --emblem-light: rgba(236, 238, 242, 0.9);
    --emblem-soft: rgba(236, 238, 242, 0.35);
  }
  html, body {
    margin: 0;
    padding: 0;
    width: 1125px;
    height: 1200px;
    overflow: hidden;
    background: var(--backdrop);
    font-family: "Roboto", Arial, sans-serif;
  }
  .canvas {
    position: relative;
    width: 1125px;
    height: 1200px;
  }
  .card {
    position: absolute;
    left: 167px;
    width: 798px;
    height: 457px;
    border-radius: 22px;
    overflow: hidden;
  }
  .card--front { top: 103px; background: var(--paper); }
  .card--back  { top: 619px; background: var(--brand-blue); }

  .brand-name {
    position: absolute;
    margin: 0;
    font-family: "Roboto", Arial, sans-serif;
    font-weight: 700;
    white-space: nowrap;
  }
  .card--front .brand-name {
    right: 56px;
    top: 66px;
    font-size: 40px;
    color: var(--brand-blue);
  }
  .card--back .brand-name {
    left: 58px;
    top: 318px;
    font-size: 38px;
    color: var(--paper);
  }

  .holder-name {
    position: absolute;
    left: 55px;
    top: 270px;
    margin: 0;
    font-family: "Roboto Condensed", "Arial Narrow", sans-serif;
    font-weight: 700;
    font-size: 30px;
    color: var(--brand-blue);
    text-transform: uppercase;
  }
  .holder-role {
    position: absolute;
    left: 55px;
    top: 303px;
    margin: 0;
    font-size: 21px;
    color: var(--sky-blue);
  }
  .divider {
    position: absolute;
    left: 55px;
    top: 339px;
    width: 687px;
    height: 2px;
    background: var(--rule-grey);
  }
  .contact-list {
    position: absolute;
    left: 55px;
    top: 355px;
    margin: 0;
    padding: 0;
    list-style: none;
    font-size: 19px;
    color: var(--ink-grey);
  }
  .contact-list li {
    display: flex;
    align-items: center;
    height: 27px;
  }
  .contact-list svg {
    width: 19px;
    height: 19px;
    margin-right: 11px;
    fill: var(--brand-blue);
  }
  .front-web {
    position: absolute;
    right: 53px;
    top: 381px;
    font-size: 18px;
    color: var(--ink-grey);
  }
  .base-stripe {
    position: absolute;
    left: 0;
    right: 0;
    bottom: 0;
    height: 22px;
    background: var(--brand-blue);
    border-top: 4px solid var(--sky-blue);
  }
  .emblem-area {
    position: absolute;
    left: 330px;
    top: 10px;
    width: 468px;
    height: 447px;
    border-radius: 50% 0 0 50%;
    background: radial-gradient(circle at 45% 50%, var(--emblem-light) 0%, var(--emblem-soft) 55%, rgba(236, 238, 242, 0) 72%);
  }
  .back-web {
    position: absolute;
    left: 68px;
    top: 383px;
    font-size: 18px;
    letter-spacing: 3px;
    color: var(--paper);
  }
</style>
</head>
<body>
<main class="canvas">
  <section class="card card--front" aria-label="Business card front">
    <p class="brand-name">MapleRidge Journeys</p>
    <h1 class="holder-name">Dolores Kwiatek</h1>
    <p class="holder-role">Travel Consultant</p>
    <div class="divider"></div>
    <ul class="contact-list">
      <li>
        <svg viewBox="0 0 24 24" aria-hidden="true"><path d="M6.6 10.8a15.1 15.1 0 0 0 6.6 6.6l2.2-2.2a1 1 0 0 1 1-.25 11.4 11.4 0 0 0 3.6.57 1 1 0 0 1 1 1V20a1 1 0 0 1-1 1A17 17 0 0 1 3 4a1 1 0 0 1 1-1h3.5a1 1 0 0 1 1 1c0 1.25.2 2.45.57 3.6a1 1 0 0 1-.25 1z"/></svg>
        (555) 418-7093
      </li>
      <li>
        <svg viewBox="0 0 24 24" aria-hidden="true"><path d="M2 6h20v13H2z M2 6l10 7 10-7" stroke="#fff" stroke-width="1.5"/></svg>
        mapleridgejourneys@examplemail.net
      </li>
    </ul>
    <span class="front-web">www.mapleridgejourneys.example</span>
    <div class="base-stripe"></div>
  </section>

  <section class="card card--back" aria-label="Business card back">
    <div class="emblem-area" role="img" aria-label="Large light brand emblem decoration"></div>
    <p class="brand-name">MapleRidge Journeys</p>
    <span class="back-web">www.mapleridgejourneys.example</span>
  </section>
</main>
</body>
</html>
```